BRIMclean - Towel Wash Package/Label Design

Design a label and look for a towel wash under the brand BRIMclean.

To be printed on either a Standup Zipper Pouch, and/or outer box.

Product Features:
Removes and Prevents Musty Odours
Increase & Restore Absorbency
Remove Buildup from Hard Water, Softeners and Detergents

Sample concept as starting point attached.

Target Market(s)

Women ages 25-55

Industry/Entity Type

Product

Font styles to use
Sans Serif
Script

Requirements
Must have
• Clean look
• Good use of one or two colours
• Imply Freshness, and Quality
• Easily identify what the products is used for.
Nice to have
• The feeling like a brand that already existed...
• Warm and welcoming colours
Should not have
• To many colour or overcomplicated deisgn

```html
<!DOCTYPE html>
<html lang="en">
<head>
<meta charset="utf-8">
<title>BRIMclean Towel &amp; Laundry Freshener</title>
<link rel="stylesheet" href="https://fonts.googleapis.com/css2?family=Montserrat:wght@500;600;800&display=swap">
<style>
  :root {
    --backdrop: #e4e4e4;
    --pouch: #141414;
    --pouch-edge: #262626;
    --orange: #d8632a;
    --green: #8dc44b;
    --green-dark: #74ad38;
    --white: #ffffff;
  }
  * { margin: 0; padding: 0; box-sizing: border-box; }
  html, body { width: 800px; height: 1200px; overflow: hidden; }
  body {
    background: var(--backdrop);
    font-family: "Montserrat", Arial, sans-serif;
    position: relative;
  }
  .pouch {
    position: absolute;
    left: 150px; top: 70px;
    width: 500px; height: 1070px;
    background: var(--pouch);
    border-radius: 10px;
  }
  .pouch-zip {
    position: absolute;
    left: 0; right: 0; top: 110px;
    height: 2px;
    background: var(--pouch-edge);
  }
  .label {
    position: absolute;
    left: 135px; top: 200px;
    width: 240px; height: 545px;
    background: var(--orange);
    padding: 0 10px 10px;
    display: flex; flex-direction: column;
  }
  .brand {
    height: 195px;
    display: flex; align-items: center; justify-content: center;
  }
  .brand-name {
    color: var(--white);
    font-weight: 800;
    font-size: 40px;
    letter-spacing: 0.5px;
  }
  .panel {
    flex: 1;
    background: var(--green);
    display: flex; flex-direction: column; align-items: center;
  }
  .product-type {
    width: 100%;
    margin-top: 12px;
    padding: 9px 0;
    background: var(--green-dark);
    color: var(--white);
    font-weight: 600;
    font-size: 11px;
    letter-spacing: 0.6px;
    text-align: center;
  }
  .sprout-icon {
    width: 70px; height: 70px;
    margin-top: 38px;
    border-radius: 50%;
    background: rgba(255,255,255,0.85);
  }
  .features {
    list-style: none;
    margin-top: 48px;
    padding: 0 22px;
    color: var(--white);
    font-weight: 500;
    font-size: 8.5px;
    line-height: 1.45;
    text-align: center;
  }
  .net-weight {
    margin-top: auto;
    margin-bottom: 16px;
    color: var(--white);
    font-weight: 500;
    font-size: 8.5px;
  }
</style>
</head>
<body>
  <div class="pouch">
    <div class="pouch-zip"></div>
    <section class="label">
      <header class="brand">
        <span class="brand-name">BRIMclean</span>
      </header>
      <div class="panel">
        <h1 class="product-type">TOWEL &amp; LAUNDRY FRESHENER</h1>
        <div class="sprout-icon" role="img" aria-label="White two-leaf sprout icon"></div>
        <ul class="features">
          <li>Removes and Prevents Musty Odours</li>
          <li>Increase &amp; Restore Absorbency</li>
          <li>Remove Buildup from Hard Water, Softeners and Detergents</li>
        </ul>
        <p class="net-weight">500g</p>
      </div>
    </section>
  </div>
</body>
</html>
```